Designer sehr zu empfehlen, engagiert und unermüdlich auf Wünsche eingehend. Gerne wieder.
Zielgruppe
Ich berate im Bereich der Telemedizin. Zielgruppe sind Ärzte, Krankenkassen, Politiker.
Aufgabenstellung
Auf der Visitenkarte sollen Adresse, e-mail, Handynummer vorhanden sein.
Briefpapier bitte im Pages-Format.

```html
<!DOCTYPE html>
<html lang="de">
<head>
<meta charset="utf-8">
<title>Corvana Telemedizin – Briefpapier und Visitenkarte</title>
<link href="https://fonts.googleapis.com/css2?family=Play:wght@400;700&display=swap" rel="stylesheet">
<style>
  :root {
    --backdrop: #a7a8aa;
    --paper: #ffffff;
    --brand-green: #97bf1e;
    --brand-grey: #6d6e70;
    --text-grey: #6f7072;
    --card-border: #8a8b8d;
  }
  * { margin: 0; padding: 0; box-sizing: border-box; }
  html, body { width: 1029px; height: 1200px; overflow: hidden; }
  body {
    position: relative;
    background: var(--backdrop);
    font-family: "Play", sans-serif;
    color: var(--text-grey);
  }
  .letterhead, .business-card, .letterhead *, .business-card * { position: absolute; }
  .letterhead {
    left: 68.5px; top: 89px; width: 720px; height: 1019px;
    background: var(--paper);
  }
  .band { background: var(--brand-green); }
  .letterhead .band-top { left: 252px; top: 0; width: 468px; height: 14px; }
  .letterhead .band-bottom { left: 252px; bottom: 0; width: 468px; height: 13px; }
  .brand { display: flex; align-items: center; gap: 10px; color: var(--brand-grey); font-weight: 400; white-space: nowrap; line-height: 1; }
  .brand-dot { position: static; border-radius: 50%; background: var(--brand-green); flex: none; }
  .letterhead .brand { right: 48px; top: 56px; font-size: 60px; }
  .letterhead .brand-dot { width: 46px; height: 46px; }
  .sender-line { left: 86px; top: 168px; font-size: 8px; white-space: nowrap; }
  .sender-line .sep { position: static; color: var(--brand-green); padding: 0 3px; }
  .contact { font-size: 10px; line-height: 13.3px; white-space: nowrap; }
  .contact p { position: static; }
  .contact .company { color: var(--brand-green); font-weight: 700; }
  .contact .gap { margin-top: 5px; }
  .contact .label { position: static; display: inline-block; width: 36px; }
  .letterhead .contact { left: 533px; top: 166px; }
  .fold-mark { left: 0; width: 17.5px; height: 1px; background: var(--brand-green); }
  .fold-mark.first { top: 360px; }
  .fold-mark.second { top: 509px; }
  .footer { top: 966px; font-size: 10px; line-height: 13.3px; white-space: nowrap; }
  .footer.col-owner { left: 258.5px; }
  .footer.col-bank { left: 418px; }
  .footer.col-iban { left: 533px; }
  .footer p { position: static; }

  .business-card {
    left: 643px; top: 411px; width: 291px; height: 185px;
    background: var(--paper);
    border: 0.6px solid var(--card-border);
  }
  .business-card .band-top { right: 0; top: 0; width: 183px; height: 6.5px; }
  .business-card .band-bottom { right: 0; bottom: 0; width: 183px; height: 7px; }
  .business-card .brand { right: 18px; top: 28px; font-size: 34px; gap: 6px; }
  .business-card .brand-dot { width: 26px; height: 26px; }
  .holder { left: 19px; top: 84px; white-space: nowrap; }
  .holder p { position: static; }
  .holder .name { font-size: 15px; line-height: 17px; }
  .holder .role { font-size: 9.7px; line-height: 12px; }
  .business-card .contact { left: 156px; top: 86px; line-height: 11px; }
  .business-card .contact .label { width: 34px; }
  .business-card .contact .gap { margin-top: 4px; }
</style>
</head>
<body>
  <section class="letterhead" aria-label="Briefpapier">
    <div class="band band-top"></div>
    <div class="brand"><span class="brand-dot"></span>Corvana</div>
    <p class="sender-line">Corvana Telemedizin<span class="sep">|</span>Ahornweg 7<span class="sep">|</span>71634 Waldheim</p>
    <div class="contact">
      <p class="company">Corvana Telemedizin</p>
      <p>Ahornweg 7</p>
      <p>71634 Waldheim</p>
      <p>Germany</p>
      <p class="gap"><span class="label">Telefon</span>07141 982210</p>
      <p><span class="label">Mobil</span>0152 36690418</p>
      <p class="gap">info@corvana-tele.de</p>
    </div>
    <div class="fold-mark first"></div>
    <div class="fold-mark second"></div>
    <div class="footer col-owner"><p>Inhaber: Jonas Probst</p><p>UST-IdNr.: DE29481573620</p></div>
    <div class="footer col-bank"><p>Bankverbindung:</p><p>Musterbank</p></div>
    <div class="footer col-iban"><p>IBAN: DE 7740 0110 2233 9081 56</p><p>BIC: XXXXXXXXXXX</p></div>
    <div class="band band-bottom"></div>
  </section>

  <section class="business-card" aria-label="Visitenkarte">
    <div class="band band-top"></div>
    <div class="brand"><span class="brand-dot"></span>Corvana</div>
    <div class="holder">
      <p class="name">Jonas Probst</p>
      <p class="role">Berufsbezeichnung</p>
    </div>
    <div class="contact">
      <p class="company">Corvana Telemedizin</p>
      <p>Ahornweg 7</p>
      <p>71634 Waldheim</p>
      <p>Germany</p>
      <p class="gap"><span class="label">Telefon</span>07141 982210</p>
      <p><span class="label">Mobil</span>0152 36690418</p>
      <p class="gap">info@corvana-tele.de</p>
    </div>
    <div class="band band-bottom"></div>
  </section>
</body>
</html>
```